Outdoor sign for Brindle Auto Restoration

I need a horizontal 4'x 8' outdoor roadside sign for my classic auto restoration business. I have uploaded colors and our logo. Needs the Brindle name, a prominent Classic AUTO RESTORATION, phone number and website. We rebuild and restore vintage cars, trucks and 4x4s. I'd like something clean but possibly retro. Classic Auto Restoration is more important than the Brindle name. It needs to be visible and readable from the street. NO CLIP ART

Target Market(s)

Customers who need their vintage care restored or upgraded. Men and women ages 25-75

Industry/Entity Type

Automotive

Colors
FFC000
F8CF3A
FAE287
FDF2CF
FEFAEE

Requirements
Must have
• Legible. Bright. Readable as a backlit 4' x 8' large horizontal sign (roughly 120cm X 240cm)
Nice to have
• Use of the Brindle logo/type, Complete or Classic before prominent AUTO RESTORATION
Should not have
• Clip art of old cars or icons. And we don't want the Brindle Logo from the website because it wont be legible from the road. I have included the Illustrator file for Brindle text in the uploads

```html
<!DOCTYPE html>
<html lang="en">
<head>
<meta charset="utf-8">
<title>Brindle Auto Restoration – Roadside Sign</title>
<link href="https://fonts.googleapis.com/css2?family=Archivo+Black&family=Orbitron:wght@900&family=Saira+Extra+Condensed:wght@800&family=Mukta:wght@600;800&display=swap" rel="stylesheet">
<style>
  :root {
    --backdrop: #3a3a3c;
    --ink: #000000;
    --white: #ffffff;
    --gold: #ffc000;
    --sun: #f8cf3a;
    --butter: #fae287;
    --stripe-dark: #3a3a3a;
    --stripe-mid: #58585a;
    --stripe-light: #818285;
  }
  html, body {
    margin: 0;
    width: 1200px;
    height: 927px;
    overflow: hidden;
    background: var(--backdrop);
  }
  .sign { display: block; width: 1200px; height: 927px; }
  .fill-sun { fill: var(--sun); }
  .fill-gold { fill: var(--gold); }
  .fill-butter { fill: var(--butter); }
  .fill-ink { fill: var(--ink); }
  .stripe-dark { fill: var(--stripe-dark); }
  .stripe-mid { fill: var(--stripe-mid); }
  .stripe-light { fill: var(--stripe-light); }
  .dash-line { fill: none; stroke: var(--ink); stroke-width: 3; stroke-dasharray: 6 5; }
  .headline-wide { font-family: "Orbitron", sans-serif; font-weight: 900; fill: var(--ink); }
  .headline-auto { font-family: "Archivo Black", sans-serif; fill: var(--ink); }
  .brand-name { font-family: "Saira Extra Condensed", sans-serif; font-weight: 800; fill: var(--ink); }
  .services { font-family: "Saira Extra Condensed", sans-serif; font-weight: 800; fill: var(--ink); font-variant: small-caps; }
  .phone-number { font-family: "Mukta", sans-serif; font-weight: 800; fill: var(--white); }
  .web-address { font-family: "Mukta", sans-serif; font-weight: 600; fill: var(--ink); }
  .icon-line { fill: none; stroke: var(--ink); stroke-width: 5; }
</style>
</head>
<body>
<svg class="sign" viewBox="0 0 2184 1688" xmlns="http://www.w3.org/2000/svg" aria-label="Brindle Auto Restoration roadside sign">
  <!-- sign base -->
  <rect class="fill-sun" x="62" y="329" width="2060" height="1029"/>

  <!-- top stripe band -->
  <polygon class="fill-ink" points="62,329 338,329 285,398 62,398"/>
  <polygon class="stripe-dark" points="358,329 630,329 578,398 305,398"/>
  <polygon class="stripe-mid" points="652,329 922,329 871,398 598,398"/>
  <polygon class="stripe-light" points="944,329 1216,329 1163,398 891,398"/>

  <!-- bottom stripe band -->
  <polygon class="fill-ink" points="62,1118 325,1118 276,1187 62,1187"/>
  <polygon class="stripe-dark" points="346,1118 605,1118 556,1187 295,1187"/>
  <polygon class="stripe-mid" points="628,1118 890,1118 840,1187 578,1187"/>
  <polygon class="stripe-light" points="911,1118 1172,1118 1120,1187 860,1187"/>

  <!-- right message panel -->
  <path class="fill-butter" d="M1212,338 C1330,450 1393,585 1393,720 C1393,880 1300,1010 1172,1118 L1120,1187 L1057,1358 L2122,1358 L2122,329 L1216,329 Z"/>
  <path class="fill-gold" d="M1222,329 C1350,500 1540,585 1750,585 C1900,585 2020,530 2122,476 L2122,329 Z"/>
  <path class="dash-line" d="M1387,538 C1500,592 1620,614 1740,614 C1890,614 2010,562 2120,512"/>
  <path class="dash-line" d="M1387,538 C1420,620 1430,680 1426,740 C1415,900 1300,1050 1145,1155"/>

  <!-- headline -->
  <text class="headline-wide" x="232" y="581" font-size="128" textLength="928" lengthAdjust="spacingAndGlyphs">CLASSIC</text>
  <text class="headline-auto" x="118" y="897" font-size="390" textLength="1156" lengthAdjust="spacingAndGlyphs">AUTO</text>
  <text class="headline-wide" x="120" y="1021" font-size="112" textLength="1098" lengthAdjust="spacingAndGlyphs">RESTORATION</text>

  <!-- brand name -->
  <text class="brand-name" x="1745" y="487" font-size="138" text-anchor="middle" textLength="570" lengthAdjust="spacingAndGlyphs">BRINDLE</text>

  <!-- services -->
  <g class="services" font-size="112" text-anchor="middle">
    <text x="1755" y="722">We Rebuild</text>
    <text x="1767" y="830">And Restore</text>
    <text x="1767" y="937">Vintage Cars,</text>
    <text x="1755" y="1043">Trucks And</text>
    <text x="1767" y="1147">4x4s</text>
  </g>

  <!-- contact bar -->
  <polygon class="fill-ink" points="62,1187 1118,1187 1057,1358 62,1358"/>
  <polygon class="fill-gold" points="1147,1187 2124,1187 2124,1358 1088,1358"/>

  <g class="phone-icon" fill="#ffffff">
    <path d="M112,1240 C100,1250 96,1268 108,1285 C122,1305 138,1318 155,1312 C162,1309 172,1302 172,1296 L156,1280 C150,1284 146,1290 140,1286 C130,1278 124,1270 120,1262 C118,1256 124,1252 128,1248 L118,1236 C116,1236 114,1238 112,1240 Z"/>
    <path d="M140,1250 A22,22 0 0 1 160,1270" fill="none" stroke="#ffffff" stroke-width="6" stroke-linecap="round"/>
    <path d="M142,1232 A40,40 0 0 1 178,1270" fill="none" stroke="#ffffff" stroke-width="6" stroke-linecap="round"/>
  </g>
  <text class="phone-number" x="218" y="1315" font-size="150" textLength="794" lengthAdjust="spacingAndGlyphs">501-555-0142</text>

  <g class="globe-icon">
    <circle class="icon-line" cx="1182" cy="1280" r="33"/>
    <ellipse class="icon-line" cx="1182" cy="1280" rx="13" ry="33"/>
    <line class="icon-line" x1="1149" y1="1280" x2="1215" y2="1280"/>
    <line class="icon-line" x1="1154" y1="1264" x2="1210" y2="1264"/>
    <line class="icon-line" x1="1154" y1="1296" x2="1210" y2="1296"/>
    <line class="icon-line" x1="1182" y1="1247" x2="1182" y2="1313"/>
  </g>
  <text class="web-address" x="1238" y="1305" font-size="96" textLength="857" lengthAdjust="spacingAndGlyphs">brindleautoworks.com</text>
</svg>
</body>
</html>
```